Lanterns and lemonades - fun, casual event near the beach to raise money for needy families

We are seeking a logo, invitation and save the date for our charity event called "Lanterns and Lemonades" set to occur on Dec 1,2017. We want to use the logo on letterhead, social media, etc.

Officially formed in 1955, our all-volunteer organization fundraises to offer a unique service in our area - providing one-time emergency assistance for those experiencing an unexpected temporary downturn.

Referrals come to us from governmental or private social service organizations as well as churches and temples. We work with social service professionals who have developed plans with their clients so they can get back on their feet after receiving our assistance. We have developed an extensive network of professionals in the community upon whom we can rely - and who in turn depend upon us for stopgap funding.

We are there when all other alternatives have been exhausted and immediate help is needed. We provide emergency assistance to those with a recovery plan in place and a goal of financial stability and thereby improving the quality of life for children, the elderly, single men and women and families in our area.

Target Market(s)

Age 35-65 affluent couples

Industry/Entity Type

Charity

Font styles to use
Decorative
Script

Colors

Designer to choose colors to be used in the design.

Requirements
Must have
• Image of margaritas and holiday themeno specific mention of "Christmas" no specific mention of "Christmas"
Nice to have
• Maybe beach-ish or water theme. Event will be at a rooftop bar along the beach.
Should not have
• no specific mention of "Christmas"

```html
<!DOCTYPE html>
<html lang="en">
<head>
<meta charset="utf-8">
<title>Lanterns and Lemonades – Invitation</title>
<link rel="stylesheet" href="https://fonts.googleapis.com/css2?family=Bodoni+Moda:wght@500;600&family=Crimson+Pro:wght@400&display=swap">
<style>
  :root {
    --paper: #ffffff;
    --ink: #111111;
    --holiday-red: #d2202e;
    --lime: #3ea843;
    --panel-light: #b6d88a;
    --panel-dark: #a8cf6a;
    --glass-green: #8cc63f;
  }
  * { margin: 0; padding: 0; box-sizing: border-box; }
  html, body {
    width: 1200px; height: 800px; overflow: hidden;
    background: var(--paper);
  }
  .invitation {
    position: relative; width: 1200px; height: 800px;
    background: var(--paper);
    font-family: "Bodoni Moda", "Didot", serif;
  }
  .frame { position: absolute; inset: 0; }
  .headline {
    position: absolute; left: 48px; top: 58px;
    color: var(--holiday-red);
    font-size: 42px; font-weight: 600; line-height: 54px;
    letter-spacing: 0.4px;
  }
  .event-name {
    position: absolute; left: 450px; top: 210px; width: 540px;
    color: var(--ink);
    font-size: 70px; font-weight: 600; line-height: 86px;
    text-align: center;
  }
  .event-mark {
    position: absolute; left: 695px; top: 408px;
    width: 50px; height: 50px; border-radius: 50%;
    background: var(--glass-green);
  }
  .info-panel {
    position: absolute; left: 75px; top: 360px; width: 383px; height: 262px;
    background: linear-gradient(to right, var(--panel-light) 0 227px, var(--panel-dark) 227px);
  }
  .info-panel p {
    position: absolute; left: 13px; top: 12px;
    font-family: "Crimson Pro", "Minion Pro", serif;
    font-size: 34px; line-height: 40px; color: var(--ink);
  }
  .details {
    position: absolute; right: 50px; top: 534px;
    color: var(--holiday-red);
    font-size: 36px; font-weight: 600; line-height: 44px;
    text-align: right; letter-spacing: 1px;
  }
  .details .time { margin-top: 6px; }
  .rsvp {
    position: absolute; left: 78px; top: 702px;
    color: var(--lime);
    font-size: 31px; font-weight: 500; letter-spacing: 0.5px;
    word-spacing: 4px;
  }
</style>
</head>
<body>
<main class="invitation">
  <svg class="frame" width="1200" height="800" viewBox="0 0 1200 800" aria-hidden="true">
    <g stroke="#111" stroke-width="1.6" fill="none">
      <polyline points="573,69 1150,69 1150,524"/>
      <polyline points="50,220 50,758 990,758"/>
    </g>
  </svg>

  <h1 class="headline">You are invited to attend<br>a holiday event<br>involving...</h1>

  <h2 class="event-name">Lanterns and Lemonades</h2>
  <span class="event-mark" aria-hidden="true"></span>

  <section class="info-panel">
    <p>A little information here<br>about the event or charity<br>affair.<br>Entertainment<br>&nbsp;or name of hosts</p>
  </section>

  <section class="details">
    <p>Friday, December 1. 2017</p>
    <p>Seabreeze Harbor Hotel</p>
    <p>Whatever, Fl</p>
    <p>Rooftop Bar</p>
    <p class="time">7:00 p.m</p>
  </section>

  <p class="rsvp">RSVP&nbsp; Delia Marchetti&nbsp; at 555.014.2290</p>
</main>
</body>
</html>
```